Business Card for Voltrix

Horizontal business card for voltrix, the electrical contractor.
clean and professional looking, using company branding and colours.
I also want the blue in the logo and wording to be made a more 'electric' blue and the grey 'Voltrix' to be slightly darker.

Pleas use the following contact details:

Colin Marsh
Owner

t: 01736 582910
m: 07831 206719
e: colin@voltrix-installs.co.uk

www.voltrix-installs.co.uk

Industry/Entity Type

Electrical

Font styles to use
Sans Serif

```html
<!DOCTYPE html>
<html lang="en">
<head>
<meta charset="utf-8">
<title>Voltrix – Business Card</title>
<link rel="stylesheet" href="https://fonts.googleapis.com/css2?family=Exo+2:wght@300;400;600&display=swap">
<style>
  :root {
    --electric-blue: #00a8ff;
    --charcoal: #3a3a3d;
    --card-white: #ffffff;
  }
  * { margin: 0; padding: 0; box-sizing: border-box; }
  html, body {
    width: 1200px;
    height: 720px;
    overflow: hidden;
    background: var(--card-white);
  }
  .card {
    position: relative;
    width: 1200px;
    height: 720px;
    background: var(--card-white);
    font-family: "Exo 2", Arial, sans-serif;
    font-weight: 300;
    color: var(--charcoal);
  }
  .brand {
    position: absolute;
    left: 73px;
    top: 72px;
    display: flex;
    align-items: center;
    gap: 16px;
  }
  .brand-dot {
    width: 102px;
    height: 102px;
    flex: none;
  }
  .brand-text { display: flex; flex-direction: column; }
  .brand-name {
    font-size: 72px;
    font-weight: 600;
    line-height: 0.9;
    letter-spacing: 0.8em;
    text-transform: uppercase;
    color: var(--charcoal);
  }
  .tagline {
    margin-top: 8px;
    font-size: 36px;
    font-weight: 400;
    line-height: 1;
    letter-spacing: 0.2em;
    text-transform: uppercase;
    color: var(--electric-blue);
    white-space: nowrap;
  }
  .person {
    position: absolute;
    left: 74px;
    top: 470px;
  }
  .person-name {
    font-size: 36px;
    line-height: 1;
    letter-spacing: 0.18em;
    color: var(--charcoal);
    white-space: nowrap;
  }
  .person-role {
    margin-top: 32px;
    font-size: 34px;
    line-height: 1;
    letter-spacing: 0.14em;
    text-transform: uppercase;
    color: var(--electric-blue);
  }
  .contact {
    position: absolute;
    left: 549px;
    top: 472px;
  }
  .contact-list { list-style: none; }
  .contact-item {
    display: flex;
    font-size: 30px;
    line-height: 29px;
    letter-spacing: 0.2em;
    white-space: nowrap;
  }
  .contact-label {
    width: 40px;
    color: var(--electric-blue);
    font-weight: 400;
  }
  .contact-value { color: var(--charcoal); }
  .website {
    margin-top: 26px;
    font-size: 27px;
    line-height: 1;
    letter-spacing: 0.27em;
    color: var(--electric-blue);
    white-space: nowrap;
  }
</style>
</head>
<body>
  <main class="card">
    <header class="brand">
      <svg class="brand-dot" viewBox="0 0 102 102" aria-hidden="true">
        <circle cx="51" cy="51" r="49" fill="var(--electric-blue)"/>
      </svg>
      <div class="brand-text">
        <span class="brand-name">Voltrix</span>
        <span class="tagline">The Electrical Contractor</span>
      </div>
    </header>

    <section class="person">
      <p class="person-name">Colin Marsh</p>
      <p class="person-role">Owner</p>
    </section>

    <section class="contact">
      <ul class="contact-list">
        <li class="contact-item"><span class="contact-label">M</span><span class="contact-value">07831 206719</span></li>
        <li class="contact-item"><span class="contact-label">T</span><span class="contact-value">01736 582910</span></li>
        <li class="contact-item"><span class="contact-label">E</span><span class="contact-value">colin@voltrix-installs.co.uk</span></li>
      </ul>
      <p class="website">www.voltrix-installs.co.uk</p>
    </section>
  </main>
</body>
</html>
```